Brightwell is a company offering Colon Hydrotherapy (or colonics)

Brightwell offers Colon Hydrotherapy using an innovative FDA approved system from the USA. The system is called the TORVA system. The clinic is based in Whangarei, Northland and is the first business of this kind for Northland.
I used to use a design from the Prontaleaf website - a water symbol. However, I want a design that will convey freshness. I want something new and clean which conveys vitality and revitalisation .... perhaps water or bubbles but which brings across the idea of detoxing (which is what colon hydrotherapy does)
The clinic will only be completed in April so for now I have put my mobile number but once in the clinic this will need to be changed to a landline number ... the email address will also change. Thanks for any ideas you give me,
Updates

Hi. I need the name Brightwell first and foremost as this is the name of the Company Underneath this it has to say Colon Hydrotherapy to let people know what Brightwell is My name underneath that would be Marian Holcombe And all contact details to follow this. Thanks !

Target Market(s)

People who are wanting to "detox" and focusing on their health and wellbeing

Industry/Entity Type

Clinic

Contact Information for Business Card

Brightwell
Colon Hydrotherapy
Marian Holcombe
Unit B, 42c Ferrand Lane, Whangarei

021 0487 3916
brightwellclinic@mailnest.example

Font styles to use
Serif

Colors
cee9f6
33a6d7
86cae6

Requirements
Must have
• Stand out with colour or logo

```html
<!DOCTYPE html>
<html lang="en">
<head>
<meta charset="utf-8">
<title>Brightwell Business Card</title>
<link rel="stylesheet" href="https://fonts.googleapis.com/css2?family=Arimo:wght@400;700&display=swap">
<style>
  :root {
    --backdrop: #e9ecef;
    --card-white: #ffffff;
    --wave-sky: #3cc3f0;
    --wave-navy: #0f0f3a;
    --lotus-light: #4aa8dc;
    --lotus-deep: #2b3e8f;
    --text-light: #ffffff;
  }
  html, body {
    margin: 0;
    padding: 0;
    width: 1200px;
    height: 1200px;
    overflow: hidden;
    background: var(--backdrop);
  }
  .canvas {
    position: relative;
    width: 1200px;
    height: 1200px;
  }
  .business-card {
    position: absolute;
    left: 94px;
    top: 288px;
    width: 1012px;
    height: 624px;
    background: var(--card-white);
    overflow: hidden;
    box-shadow: 0 6px 18px rgba(0, 0, 0, 0.18);
  }
  .card-waves {
    position: absolute;
    inset: 0;
    width: 100%;
    height: 100%;
  }
  .wave-sky { fill: var(--wave-sky); }
  .wave-navy { fill: var(--wave-navy); }
  .lotus-artwork {
    position: absolute;
    left: 200px;
    top: 70px;
    width: 620px;
    height: 312px;
  }
  .card-details {
    position: absolute;
    left: 0;
    top: 398px;
    width: 950px;
    text-align: center;
    color: var(--text-light);
    font-family: "Arimo", Arial, sans-serif;
  }
  .card-company {
    margin: 0 0 6px;
    font-size: 36px;
    line-height: 1.1;
    font-weight: 700;
    letter-spacing: 0.3px;
  }
  .card-service {
    margin: 0 0 10px;
    font-size: 22px;
    line-height: 1.15;
    font-weight: 700;
    letter-spacing: 1px;
  }
  .card-line {
    margin: 0 0 5px;
    font-size: 24px;
    font-weight: 400;
    line-height: 1.15;
  }
</style>
</head>
<body>
<main class="canvas">
  <section class="business-card">
    <svg class="card-waves" viewBox="0 0 843 520" preserveAspectRatio="none" aria-hidden="true">
      <path class="wave-sky" d="M0,225 C150,290 330,310 480,290 C620,270 720,180 843,215 L843,520 L0,520 Z"/>
      <path class="wave-navy" d="M0,225 C140,290 300,305 470,295 C640,285 760,330 843,400 L843,520 L0,520 Z"/>
    </svg>

    <svg class="lotus-artwork" viewBox="0 0 620 312" role="img" aria-label="Blue lotus flower illustration with sweeping leaf shapes">
      <defs>
        <linearGradient id="lotus-fill" x1="0" y1="0" x2="0" y2="1">
          <stop offset="0" stop-color="#4aa8dc"/>
          <stop offset="1" stop-color="#2b3e8f"/>
        </linearGradient>
      </defs>
      <ellipse cx="310" cy="170" rx="300" ry="140" fill="url(#lotus-fill)" opacity="0.9"/>
    </svg>

    <div class="card-details">
      <p class="card-company">Brightwell</p>
      <p class="card-service">Colon Hydrotherapy</p>
      <p class="card-line">Marian Holcombe</p>
      <p class="card-line">Unit B, 42c Ferrand Lane, Whangarei</p>
      <p class="card-line">021 0487 3916</p>
      <p class="card-line">brightwellclinic@mailnest.example</p>
    </div>
  </section>
</main>
</body>
</html>
```